Web Design Project - brivocell

I'm building an agency for marketing solutions but also medical education and patients education for pharmaceutical companies, medical societies and patient advocacy groups. We want to be perceived as the most innovative in the market. We work through design thinking solutions for campaigns and services.
I love some websites based on Swiss style design like www.plumvane.example
We are a small group of designers, physicians and creatives working together to deliver the best experiences in our market.
We decided to also use pixel forum expecting that we maybe found a great idea we didn't thought about yet.

I'm extending it for more 2 weeks

Reason: I need the best design you can. Only PSD. No code needed. Love Swiss style, like tessera 5 and plumvane.example I'm extending the deadline until get something great. Willing to extend as much as needed.

Target Market(s)

Pharmaceutical companies, physicians, medical societies, patients advocacy groups

Industry/Entity Type

Pharmaceutical

Font styles to use
Other font styles liked:
• Helvetia family

Colors

Designer to choose colors to be used in the design.

Requirements
Must have
• Must be innovative like www.plumvane.example
Nice to have
• Cool menus
Should not have
• Not to appear too much Comercial. We like to be a boutique in this market. Craftsmen working with less clients at time but delivering precious stones.

```html
<!DOCTYPE html>
<html lang="en">
<head>
<meta charset="utf-8">
<title>brivocell — Medical &amp; Patients Education</title>
<link href="https://fonts.googleapis.com/css2?family=Oswald:wght@300;400&family=Roboto:wght@300;400&family=Lato:wght@400;700&display=swap" rel="stylesheet">
<style>
  :root{
    --page:#1f1f1f;
    --tile:#363636;
    --coral:#e85a4a;
    --coral-band:rgba(232,90,74,.85);
    --pale:#e4e4e8;
    --navy:#24344a;
    --sky:#3aaee6;
    --ink:#2b2b2b;
    --muted:#6c6c6c;
    --white:#ffffff;
  }
  *{box-sizing:border-box;margin:0;padding:0}
  html,body{width:833px;height:1200px;overflow:hidden;background:var(--page)}
  body{position:relative;font-family:'Roboto',Arial,sans-serif;color:var(--white)}
  .box{position:absolute}
  .display{font-family:'Oswald','Arial Narrow',sans-serif;font-weight:300;text-transform:uppercase;letter-spacing:-.3px}

  /* header */
  .brand{background:var(--coral);display:flex;align-items:center;justify-content:center;font-size:38px;color:var(--white)}
  .nav-item{background:var(--tile);display:flex;flex-direction:column;align-items:center;justify-content:center;gap:8px;font-size:13.5px;text-transform:uppercase;letter-spacing:.2px}
  .nav-item svg{width:28px;height:28px;fill:#fff}

  /* welcome */
  .welcome{background:var(--pale);padding:24px 18px 0 18px;color:var(--ink)}
  .welcome h1{font-size:20px;color:#222}
  .welcome h1 span{color:var(--coral)}
  .welcome h2{font-size:11.5px;font-weight:400;text-transform:uppercase;line-height:16px;margin:12px 0 11px 2px;color:#333}
  .body-copy{font-size:12px;font-weight:300;line-height:17.8px;text-align:justify}
  .welcome .body-copy{color:var(--muted)}
  .more{color:var(--coral);font-style:italic}

  /* photos */
  .photo{overflow:hidden}
  .hero-photo{background:linear-gradient(115deg,#b9c9d6 0%,#f1f3f4 30%,#d9b8a2 52%,#f0e2d2 70%,#c7d2da 100%)}
  .caption-bar{left:0;right:0;bottom:0;height:36px;background:rgba(30,34,40,.85);display:flex;align-items:center}
  .arrows{width:60px;height:100%;background:#1d2640;display:flex;align-items:center;justify-content:space-around;padding:0 8px}
  .arrows svg{width:10px;height:10px;stroke:#fff;stroke-width:2.5;fill:none}
  .caption-bar p{flex:1;text-align:center;font-size:14.5px;font-weight:300;letter-spacing:-.4px}
  .label-band{left:0;right:0;bottom:0;height:45px;background:var(--coral-band);display:flex;align-items:center;padding-left:11px;font-size:19.5px}

  /* about */
  .about{background:var(--coral);padding:20px 16px 0 16px}
  .about h3{font-size:21px;margin-bottom:10px}
  .about .body-copy{color:#fde9e6}

  /* video */
  .video-text{background:var(--white);padding:26px 27px 0 42px;color:var(--ink)}
  .video-tag{left:0;top:29px;width:29px;height:28px;background:var(--coral);display:flex;align-items:center;justify-content:center}
  .video-text h3{font-size:21px;line-height:25px;color:#2a2a2a;margin-bottom:14px}
  .video-text .body-copy{color:var(--muted)}
  .actions{background:var(--navy);display:flex;flex-direction:column;align-items:center;padding-top:20px;gap:20px;font-size:12px}
  .action{display:flex;flex-direction:column;align-items:center;gap:5px}
  .action svg{width:26px;height:26px;fill:none;stroke:#fff;stroke-width:2}
  .video-photo{background:linear-gradient(90deg,#9fb2c2 0%,#d6dee4 30%,#c9d4dc 50%,#e6cdb8 68%,#f3f4f5 82%,#8fa4b8 100%)}
  .play{left:123px;top:92px;width:46px;height:46px;border-radius:50%;background:#1d2a40;display:flex;align-items:center;justify-content:center}

  /* tweet */
  .tweet{background:var(--sky);padding:32px 30px 0 19px;font-family:'Lato',Arial,sans-serif}
  .tweet p{font-size:13px;line-height:15.5px}
  .tweet time{display:block;margin-top:16px;font-size:10.5px;color:#d7efff}
  .tweet-source{left:22px;top:162px;font-size:14px;font-weight:700}

  /* footer */
  .footer-brand{font-size:31px}
  .newsletter{background:var(--tile);text-align:center;padding-top:10px}
  .newsletter h4{font-size:21px;text-transform:none;font-weight:300}
  .newsletter small{display:block;font-size:7.5px;margin-top:6px}
  .signup{display:flex;gap:10px;margin:15px 0 0 17px}
  .signup span{width:199px;height:27px;border:1px solid #8a8a8a;text-align:left;font-size:11.5px;color:#9a9a9a;padding:6px 12px;font-weight:300}
  .signup b{width:67px;height:27px;background:var(--coral);font-size:10.5px;font-weight:400;line-height:27px}
  .social{background:var(--tile);display:flex;flex-direction:column;align-items:center;padding-top:24px}
  .social ul{list-style:none;display:flex;gap:11px}
  .social li{width:35px;height:35px;display:flex;align-items:center;justify-content:center;font-size:8.5px}
  .social .copyright{font-family:'Oswald',sans-serif;font-size:11px;margin-top:18px;font-weight:300}
</style>
</head>
<body>

<header>
  <div class="box brand display" style="left:69px;top:18px;width:224px;height:80px">brivocell</div>
  <nav>
    <div class="box nav-item" style="left:303px;top:18px;width:105px;height:80px">
      <svg viewBox="0 0 24 24"><path d="M12 3 2 12h3v8h5v-5h4v5h5v-8h3z"/></svg>Home</div>
    <div class="box nav-item" style="left:420px;top:18px;width:106px;height:80px">
      <svg viewBox="0 0 24 24"><circle cx="9" cy="8" r="4"/><circle cx="17" cy="9" r="3"/><path d="M1 21c0-5 4-8 8-8s8 3 8 8zM18 13c3 0 5 3 5 7h-4c0-3-1-5-3-7z"/></svg>About</div>
    <div class="box nav-item" style="left:538px;top:18px;width:105px;height:80px">
      <svg viewBox="0 0 24 24"><path d="M10 2h4l.6 3 2.2 1.2 2.8-1.4 2.8 2.8-1.4 2.8L22 12.6V15l-3 .6-1.2 2.2 1.4 2.8-2.8 2.8-2.8-1.4L14 22h-4l-.6-3-2.2-1.2-2.8 1.4-2.8-2.8 1.4-2.8L2 14v-4l3-.6 1.2-2.2-1.4-2.8 2.8-2.8 2.8 1.4L10 2zm2 7a3 3 0 1 0 0 6 3 3 0 0 0 0-6z"/></svg>Services</div>
    <div class="box nav-item" style="left:654px;top:18px;width:106px;height:80px">
      <svg viewBox="0 0 24 24"><path d="M12 1a11 11 0 1 0 0 22 11 11 0 0 0 0-22zm0 2a9 9 0 1 1 0 18 9 9 0 0 1 0-18zM8 6l2 3-1.2 1.4c.8 1.8 2 3 3.8 3.8L14 13l3 2-1 2.5C11 17.5 6.5 13 6.5 8z"/></svg>Contacts</div>
  </nav>
</header>

<main>
  <section class="box welcome" style="left:70px;top:110px;width:223px;height:248px">
    <h1 class="display">Welcome to <span>brivocell</span></h1>
    <h2>Medical societies and<br>patient advocacy groups</h2>
    <p class="body-copy">Lorem Ipsum is simply dummy text of the printing and typesetting industry. Lorem ipsum has been the industry's type and scrambled it to make a type specimen book. It has survived not onlyfive centuries, but also the leap .. <span class="more">Read more</span></p>
  </section>

  <section class="box photo hero-photo" style="left:303px;top:110px;width:457px;height:248px" role="img" aria-label="Smiling doctor and nurse holding a red heart together in a clinic">
    <div class="box caption-bar">
      <div class="arrows">
        <svg viewBox="0 0 10 10"><path d="M7 1 3 5l4 4"/></svg>
        <svg viewBox="0 0 10 10"><path d="M3 1l4 4-4 4"/></svg>
      </div>
      <p class="display">Medical education and patients education for pharmaceutical</p>
    </div>
  </section>

  <section class="box photo" style="left:70px;top:370px;width:223px;height:224px;background:linear-gradient(160deg,#c7ccd0 0%,#e3c6b1 28%,#f4f5f6 55%,#8e9fb5 80%,#d4d9dd 100%)" role="img" aria-label="Team of doctors in white coats">
    <div class="box label-band display">Medical education</div>
  </section>

  <section class="box about" style="left:303px;top:370px;width:223px;height:224px">
    <h3 class="display">About us</h3>
    <p class="body-copy">Lorem Ipsum is simply dummy text of the printing and typesetting industry. Lorem ipsum has been the industry's type and scrambled it to make a type specimen book. It has survived not only five centuries, but also the leap into electronic typesetting, <span style="font-style:italic">.. Read more</span></p>
  </section>

  <section class="box photo" style="left:536px;top:370px;width:223px;height:224px;background:linear-gradient(120deg,#c2c8c6 0%,#e9ecec 30%,#a7aeb6 55%,#eef0f1 70%,#3f4c63 100%)" role="img" aria-label="Doctor assisting an elderly patient in a wheelchair">
    <div class="box label-band display">Patients education</div>
  </section>

  <section class="box video-text" style="left:71px;top:603px;width:233px;height:223px">
    <div class="box video-tag"><svg width="15" height="10" viewBox="0 0 15 10"><rect width="10" height="10" fill="#fff"/><path d="M10 5 15 1v8z" fill="#fff"/></svg></div>
    <h3 class="display">Pharmaceutical<br>video</h3>
    <p class="body-copy">Lorem Ipsum is simply dummy text of the printing and typesetting industry. Lorem ipsum has been the industry's type and scrambled it to make a type specimen book. It has also the leap.. <span class="more" style="font-style:normal">Read more</span></p>
  </section>

  <aside class="box actions" style="left:304px;top:603px;width:81px;height:223px">
    <div class="action"><svg viewBox="0 0 24 24"><path d="M12 21 3.5 12.5a5 5 0 0 1 8.5-6 5 5 0 0 1 8.5 6z"/></svg>Like</div>
    <div class="action"><svg viewBox="0 0 24 24"><circle cx="12" cy="12" r="10"/><path d="M12 6v6H8"/></svg>Later</div>
    <div class="action"><svg viewBox="0 0 24 24"><path d="M3 10v11h16v-5"/><path d="M8 16c0-5 4-8 10-8M15 4l4 4-4 4"/></svg>Share</div>
  </aside>

  <section class="box photo video-photo" style="left:385px;top:603px;width:373px;height:223px" role="img" aria-label="Video still of a smiling doctor with colleagues behind him">
    <div class="box play"><svg width="18" height="20" viewBox="0 0 18 20"><path d="M2 1 17 10 2 19z" fill="#fff"/></svg></div>
  </section>

  <section class="box photo" style="left:70px;top:836px;width:223px;height:222px;background:linear-gradient(135deg,#f1ece6 0%,#d9b59c 30%,#b9c2cc 55%,#5f7a98 80%,#c9a27c 100%)" role="img" aria-label="Elderly man seated at a desk">
    <div class="box label-band display">Patient advocacy groups</div>
  </section>

  <section class="box photo" style="left:303px;top:836px;width:223px;height:222px;background:linear-gradient(160deg,#b7bec4 0%,#e1c0a6 25%,#f5f6f7 50%,#2f8fb0 72%,#d8dde0 100%)" role="img" aria-label="Group of smiling doctors and nurses">
    <div class="box label-band display">Medical societies</div>
  </section>

  <section class="box tweet" style="left:536px;top:836px;width:223px;height:222px">
    <p>Saturday Career Workshops are back at NLC! See what high school students created this week: <b>http://go.brv.example/Xx1EsL</b></p>
    <time>6 hours ago</time>
    <div class="box tweet-source">Chirp</div>
  </section>
</main>

<footer>
  <div class="box brand display footer-brand" style="left:71px;top:1071px;width:147px;height:115px">brivocell</div>
  <div class="box newsletter" style="left:229px;top:1071px;width:310px;height:115px">
    <h4 class="display">Join the Newsletter</h4>
    <small>Sign up for our personalized daily newsletter</small>
    <div class="signup"><span>Enter email address</span><b>SIGN UP</b></div>
  </div>
  <div class="box social" style="left:550px;top:1071px;width:209px;height:115px">
    <ul>
      <li style="background:#3b5ba5">Pulse</li>
      <li style="background:#2aa9e0">Chirp</li>
      <li style="background:#1ab7ea">Reel</li>
      <li style="background:#f7a531">Feed</li>
    </ul>
    <p class="copyright">Copyright © 2014. All Rights reserved.</p>
  </div>
</footer>

</body>
</html>
```